Gymnastics Award Design Needed--for kids

Need a gymnastics certificate or award designed. Will be printed on a piece of 8.5x11 paper. The award will be celebrating the gymnast learning a new skill in gymnastics. So it should be fun, but still look "official". Needs to look good hanging on a gymnast's bedroom wall.

It should say "The Aerial Cartwheel Club"
I will be using this design to change it based on the skill.

My main colors are:
#34475D
#E1467A
#7555A4

So should use those, but can add others

My website is tumblenest.net so you can see the look/feel.

Target Market(s)

Main audience will be girls ages 5-12, but will also be used by slightly older girls and boys. So needs to be fun, not too gender specific.

Industry/Entity Type

Learning

Requirements
Must have
• The following will need to go on the certificate:
• * Name of Skill
• * Image of Skill
• * Gymnast's Name
• * my logo
• * Gym's Logo
• * Gym's Name
• Optional: Date

```html
<!DOCTYPE html>
<html lang="en">
<head>
<meta charset="utf-8">
<title>The Aerial Cartwheel Club – Certificate of Completion</title>
<link rel="stylesheet" href="https://fonts.googleapis.com/css2?family=Lilita+One&family=Dancing+Script:wght@600;700&family=Alfa+Slab+One&family=Open+Sans:wght@400;600&display=swap">
<style>
  :root {
    --backdrop: #65045f;
    --violet-deep: #3f1d9e;
    --violet: #7555a4;
    --violet-bright: #8a3fd1;
    --paper: #f5f2ef;
    --pink: #e1467a;
    --title-red: #d8245a;
    --ink-blue: #2e1a8c;
    --navy: #34475d;
    --ink: #1b1b1b;
    --body: #2a2a2a;
    --gym-blue: #1f3fa8;
  }
  * { margin: 0; padding: 0; box-sizing: border-box; }
  html, body {
    width: 800px; height: 1200px; overflow: hidden;
    background: var(--backdrop);
  }
  .certificate {
    position: absolute; left: 40px; top: 321px;
    width: 720px; height: 558px;
    background:
      radial-gradient(ellipse at 50% 0%, rgba(200,150,255,.55), rgba(200,150,255,0) 60%),
      linear-gradient(180deg, var(--violet-bright) 0%, #5a2cc2 55%, var(--violet-deep) 100%);
    box-shadow: 0 8px 24px rgba(0,0,0,.35);
    overflow: hidden;
  }
  .certificate__paper { position: absolute; inset: 0; }
  .certificate__title {
    position: absolute; left: 0; top: 92px; width: 720px; height: 80px;
  }
  .certificate__title text {
    font-family: "Lilita One", sans-serif; font-size: 35px;
    fill: var(--title-red); letter-spacing: 1px;
  }
  .skill-illustration {
    position: absolute; left: 252px; top: 150px; width: 215px; height: 70px;
    background: linear-gradient(90deg, rgba(225,70,122,.25), rgba(232,190,160,.45), rgba(225,70,122,.25));
    border-bottom: 2px solid #8a7f70;
    border-radius: 4px 4px 0 0;
  }
  .certificate__heading {
    position: absolute; left: 0; width: 720px; top: 222px;
    text-align: center;
    font-family: "Dancing Script", cursive; font-weight: 700; font-size: 48px;
    line-height: 58px;
    color: var(--ink-blue);
  }
  .certificate__presented {
    position: absolute; left: 0; width: 720px; top: 288px;
    text-align: center;
    font-family: "Open Sans", sans-serif; font-size: 16px; color: var(--body);
  }
  .certificate__recipient {
    position: absolute; left: 166px; width: 387px; top: 308px;
    padding-bottom: 2px;
    text-align: center; border-bottom: 1.5px solid var(--ink);
    font-family: "Alfa Slab One", serif; font-size: 27px;
    letter-spacing: 1.5px; color: var(--ink);
  }
  .certificate__details {
    position: absolute; left: 0; width: 720px; top: 358px;
    text-align: center;
    font-family: "Open Sans", sans-serif; font-size: 16px; line-height: 22px;
    color: var(--body);
  }
  .brand-mark {
    position: absolute; left: 92px; top: 418px;
    display: flex; align-items: center; gap: 10px;
  }
  .brand-mark__dot {
    width: 26px; height: 26px; border-radius: 50%; background: var(--violet);
  }
  .brand-mark__name {
    font-family: "Open Sans", sans-serif; font-weight: 400; font-size: 25px;
    color: var(--pink); letter-spacing: .5px; text-transform: uppercase;
  }
  .gym-sign {
    position: absolute; left: 452px; top: 422px; width: 170px;
    text-align: center;
  }
  .gym-sign__signature {
    font-family: "Dancing Script", cursive; font-weight: 600; font-size: 22px;
    color: var(--ink);
    border-bottom: 1.2px solid var(--ink); line-height: 28px;
  }
  .gym-mark {
    margin-top: 6px;
    display: flex; align-items: center; justify-content: center; gap: 6px;
  }
  .gym-mark__square { width: 16px; height: 16px; background: var(--gym-blue); }
  .gym-mark__name {
    font-family: "Open Sans", sans-serif; font-weight: 600; font-size: 15px;
    color: var(--gym-blue); white-space: nowrap;
  }
</style>
</head>
<body>
  <main class="certificate">
    <svg class="certificate__paper" width="720" height="558" viewBox="0 0 720 558" aria-hidden="true">
      <path d="M75 98 Q360 60 660 72 Q668 280 655 488 Q360 478 68 492 Q60 300 75 98 Z"
            fill="var(--paper)" stroke="var(--pink)" stroke-width="3"/>
    </svg>

    <svg class="certificate__title" viewBox="0 0 720 80" aria-label="The Aerial Cartwheel Club">
      <path id="title-arc" d="M100 74 Q370 12 640 60" fill="none"/>
      <text text-anchor="middle"><textPath href="#title-arc" startOffset="50%">THE AERIAL CARTWHEEL CLUB</textPath></text>
    </svg>

    <div class="skill-illustration" role="img" aria-label="Illustration of a gymnast performing the aerial cartwheel in sequence"></div>

    <h1 class="certificate__heading">Certificate of Completion</h1>
    <p class="certificate__presented">Presented to</p>
    <p class="certificate__recipient">MIA CARTER</p>
    <p class="certificate__details">for successfully completing the Gymnastics Sessions at<br>Maple Leap Gymnastics Gym from January 1 to February 17, 2017.</p>

    <div class="brand-mark">
      <span class="brand-mark__dot"></span>
      <span class="brand-mark__name">Tumble Nest</span>
    </div>

    <div class="gym-sign">
      <p class="gym-sign__signature">Maple Leap Gym</p>
      <div class="gym-mark">
        <span class="gym-mark__square"></span>
        <span class="gym-mark__name">Maple Leap Gym</span>
      </div>
    </div>
  </main>
</body>
</html>
```